Email Marketing for HR and Career Consulting Company

I am looking for a email marketing template that will be developed in HTML format. Right now, we need PSD file format.

The content will include:

1. Featured / Poplar Blog post
2. Latest blog post this week
3. Latest jobs this week
4. Connect with us (social media)

This is a bi-weekly template which we will be sending to people who sign up our weekly newsletter. The purpose of the newsletter is to provide career advise and also latest jobs that's available from our company so that we can redirect them to our career page or apply to our latest jobs.
Updates

Project Deadline Extended
Reason: I am extending this deadline as I would like to see more designs. So far, I have only shortlisted one design that is close to what I am looking for. To all designers, please note that your design would have to be practical and easy to navigate. It also must take into consideration that when we develop this into html, it will b responsive.

Target Market(s)

Job seekers - age group 25 - 45

Industry/Entity Type

Consulting

Font styles to use
Other font styles liked:
• Helvetical

Colors
0492cd
e34197
ec1f27
85cae6
33a6d7
85acd3
eda3c7
e667a6
f59195

Requirements
Must have
• 1. Social media icons
• 2. Links - jobs, contact us
• 3. Popular career advice
• 4. Latest career advice
• 5. Featured jobs
• 6. Popular jobs
Nice to have
• I would like to see clean and minimalist design. Please try to avoid black color. Use pastel colors as much as possible. Our website is www.careerplume.com.sg
Should not have
• Should avoid black and dark colors

```html
<!DOCTYPE html>
<html lang="en">
<head>
<meta charset="utf-8">
<title>careerplume — Weekly Newsletter</title>
<link rel="stylesheet" href="https://fonts.googleapis.com/css2?family=Arimo:wght@400;700&display=swap">
<style>
  :root {
    --brand-blue: #33a6d7;
    --brand-deep: #0492cd;
    --sky-pale: #85cae6;
    --pink-soft: #eda3c7;
    --text-title: #3a3f44;
    --text-body: #7b8288;
    --text-meta: #8a9196;
    --rule: #33a6d7;
    --page: #ffffff;
  }
  * { box-sizing: border-box; margin: 0; padding: 0; }
  html, body { width: 805px; height: 1200px; overflow: hidden; background: var(--page); }
  body { font-family: "Arimo", Helvetica, Arial, sans-serif; color: var(--text-body); position: relative; }

  .newsletter { position: absolute; left: 107px; top: 0; width: 586px; height: 1200px; }

  .preheader { position: absolute; top: 14px; left: 0; right: 0; font-size: 9.5px; color: var(--text-meta); display: flex; justify-content: space-between; }
  .preheader a { color: var(--brand-deep); text-decoration: underline; }

  .masthead { position: absolute; top: 40px; left: 0; width: 586px; height: 60px; background: var(--brand-blue); display: flex; align-items: center; justify-content: space-between; padding: 0 18px; }
  .brand { font-size: 30px; font-weight: 700; color: #ffffff; letter-spacing: -0.5px; }
  .main-nav { display: flex; gap: 26px; }
  .main-nav a { color: #ffffff; text-decoration: none; font-size: 15px; letter-spacing: 0.5px; }

  .issue-bar { position: absolute; top: 106px; left: 0; right: 0; display: flex; justify-content: space-between; align-items: center; }
  .issue-date { font-size: 10.5px; font-weight: 700; color: var(--brand-deep); letter-spacing: 0.3px; }
  .social-links { display: flex; gap: 6px; }
  .social-links span { width: 15px; height: 15px; border-radius: 50%; background: var(--brand-blue); display: block; }

  .section-rule { position: absolute; left: 0; right: 0; height: 2px; background: var(--rule); }
  .section-label { position: absolute; background: var(--brand-blue); color: #ffffff; font-size: 14px; letter-spacing: 0.6px; padding: 0 12px; height: 24px; line-height: 24px; }

  .thumb { position: absolute; }
  .article { position: absolute; }
  .article h2 { font-size: 15px; font-weight: 400; color: var(--text-title); line-height: 1.3; margin-bottom: 10px; }
  .article p { font-size: 10.5px; line-height: 1.65; color: var(--text-body); }
  .btn { position: absolute; background: var(--brand-blue); color: #ffffff; font-size: 10.5px; font-weight: 700; text-decoration: none; height: 22px; line-height: 22px; padding: 0 10px; border-radius: 2px; }
  .btn-wide { padding: 0 18px; height: 28px; line-height: 28px; font-size: 11px; letter-spacing: 0.4px; }
</style>
</head>
<body>
<main class="newsletter">
  <div class="preheader">
    <span>Having trouble viewing this email? <a href="#">View it in your browser</a></span>
    <a href="#">Forward to a Friend</a>
  </div>

  <header class="masthead">
    <div class="brand">careerplume</div>
    <nav class="main-nav"><a href="#">JOBS</a><a href="#">CONTACT US</a></nav>
  </header>

  <div class="issue-bar">
    <span class="issue-date">WEEKLY NEWSLETTER - AUGUST 30,2016</span>
    <div class="social-links" aria-label="Social media links">
      <span></span><span></span><span></span><span></span><span></span><span></span>
    </div>
  </div>

  <div class="section-rule" style="top:144px"></div>
  <div class="section-label" style="top:133px;left:0">POPULAR CAREER ADVICE</div>

  <!-- Popular article 1 -->
  <div class="thumb" role="img" aria-label="Photo of a man in a suit adjusting his tie" style="left:0;top:193px;width:260px;height:196px;background:linear-gradient(135deg,#4a4a48 0%,#8b8680 45%,#c9c3ba 100%);"></div>
  <article class="article" style="left:290px;top:214px;width:290px;">
    <h2>The Interview Process, Part 2: Inside the Interviewer's Playbook</h2>
    <p>Today, we will be focusing on that mysterious, perhaps at times intimidating, character that is the interviewer. Everyone can benefit from getting a quick look inside the typical interviewer's mind ...</p>
  </article>
  <a class="btn" href="#" style="left:290px;top:360px;">Read More</a>

  <!-- Popular article 2 -->
  <article class="article" style="left:0;top:478px;width:290px;">
    <h2>Always Be Employed</h2>
    <p>The best way to get a job is to have a job". This is something that gets reiterated time and time again. A sentence that implies, right from the very beginning, that unemployed job ...</p>
  </article>
  <a class="btn" href="#" style="left:218px;top:600px;">Read More</a>
  <div class="thumb" role="img" aria-label="Photo of colleagues at a board covered in sticky notes" style="left:322px;top:434px;width:264px;height:192px;background:linear-gradient(120deg,#d9d4cc 0%,#f2e27a 40%,#c9d9a8 65%,#e8e6e2 100%);"></div>

  <a class="btn btn-wide" href="#" style="left:226px;top:676px;">VIEW ALL ADVICE</a>

  <div class="section-rule" style="top:779px"></div>
  <div class="section-label" style="top:768px;right:0">LATEST CAREER ADVICE</div>

  <!-- Latest article 1 -->
  <div class="thumb" role="img" aria-label="Illustration of a magnifying glass over job listings" style="left:38px;top:840px;width:180px;height:180px;border-radius:50%;background:radial-gradient(circle at 45% 40%,#ffffff 0%,#d7ecf5 45%,#85cae6 100%);"></div>
  <article class="article" style="left:290px;top:870px;width:290px;">
    <h2>Contract Jobs: Can They Really Be A Career Option?</h2>
    <p>Making a career out of contract jobs isn't out of the realm of possibility. While it does involve a lot of work, the payoff, the joy of entrepreneurship, is hard to match. But where to start? How do you keep it going? ...</p>
  </article>
  <a class="btn" href="#" style="left:290px;top:1002px;">Read More</a>

  <!-- Latest article 2 -->
  <article class="article" style="left:0;top:1078px;width:300px;">
    <h2>Things to Expect After You have Quit Your Job 10</h2>
    <p>Congratulations! You have quit your job and you are taking a well-deserved break. There are a lot of reasons why someone would quit a job. It can be because of a lack of interest, change of career path or simply that you need to take time off ...</p>
  </article>
  <div class="thumb" role="img" aria-label="Illustration of a person with a speech bubble saying goodbye" style="left:362px;top:1060px;width:190px;height:190px;border-radius:50%;background:radial-gradient(circle at 50% 45%,#f3f3f3 0%,#cfe6f1 55%,#33a6d7 100%);"></div>
</main>
</body>
</html>
```